Real estate broker business card

Want a modern celan but effective business card for my residential and commercial real estate business. I want the back of the card to advertise my services and to capture business. I have attached the back of my current business card fore ideas
Updates

Target Market(s)

home buyers and seller. commercial buyers and sellers

Industry/Entity Type

Real Estate

Contact Information for Business Card

must have my contact information and my photo

Requirements
Must have
• Lorna Vettridge
• Owner & Qualifying Broker
• Brockhill Real Estate Services
• 555.218.7094
• lorna@brockhillhomes.example
• www.brockhillhomes.example
Nice to have
• metallic
• Business capture text: " Don't buy or lease property without someone looking out for your best interests. I will represent you on your home or investment purchase for FREE!"
• "Home owners, call today to receive a FREE market analysis for your homes value!

```html
<!DOCTYPE html>
<html lang="en">
<head>
<meta charset="utf-8">
<title>Brockhill Real Estate Services – Business Card</title>
<link rel="stylesheet" href="https://fonts.googleapis.com/css2?family=Cinzel:wght@400&family=PT+Sans:wght@400&display=swap">
<style>
  :root {
    --bg: #8a8a8a;
    --teal: #148695;
    --teal-dark: #0a6572;
    --teal-light: #22a3b2;
    --ink: #555a5e;
    --white: #ffffff;
    --silver-1: #f4f4f4;
    --silver-2: #a9adb1;
    --photo-1: #3f5b34;
    --photo-2: #1e2a1a;
    --photo-3: #d8d2cc;
  }
  * { box-sizing: border-box; margin: 0; padding: 0; }
  html, body { width: 1200px; height: 950px; overflow: hidden; }
  body {
    background: radial-gradient(ellipse at 50% 40%, #a3a3a3 0%, var(--bg) 70%, #6f6f6f 100%);
    font-family: "PT Sans", Arial, sans-serif;
    position: relative;
  }
  .card {
    position: absolute;
    left: 270px;
    width: 660px;
    height: 377px;
    overflow: hidden;
    box-shadow: 0 10px 24px rgba(0,0,0,.35);
  }

  /* Back of card */
  .card-back {
    top: 68px;
    background: radial-gradient(ellipse at 45% 35%, var(--teal-light) 0%, var(--teal) 45%, var(--teal-dark) 100%);
    color: var(--white);
  }
  .card-back .brand {
    position: absolute;
    left: 0; right: 0; top: 120px;
    display: flex; align-items: center; justify-content: center; gap: 16px;
  }
  .brand-dot {
    width: 46px; height: 46px; border-radius: 50%;
    background: var(--white);
    flex: none;
  }
  .brand-name {
    font-family: "Cinzel", Georgia, serif;
    font-weight: 400;
    font-size: 27px;
    line-height: 1.1;
    letter-spacing: .5px;
  }
  .card-back .brand-name { color: var(--white); }
  .offer {
    position: absolute;
    left: 0; right: 0; top: 228px;
    text-align: center;
    font-size: 15.5px;
    line-height: 1.35;
  }

  /* Front of card */
  .card-front {
    top: 505px;
    background: var(--white);
  }
  .front-bands { position: absolute; inset: 0; }
  .card-front .brand {
    position: absolute;
    left: 45px; top: 120px;
    display: flex; align-items: center; gap: 12px;
    width: 340px;
  }
  .card-front .brand-dot { background: var(--teal); width: 40px; height: 40px; }
  .card-front .brand-name { color: var(--teal); font-size: 22px; }
  .portrait {
    position: absolute;
    left: 425px; top: 22px;
    width: 210px; height: 190px;
    border-radius: 14px;
    background:
      radial-gradient(ellipse at 50% 85%, var(--photo-3) 0%, rgba(216,210,204,0) 45%),
      radial-gradient(ellipse at 30% 30%, var(--photo-1) 0%, var(--photo-2) 100%);
  }
  .contact-list {
    position: absolute;
    left: 45px; top: 222px;
    list-style: none;
    color: var(--ink);
    font-size: 14px;
    line-height: 22px;
  }
  .contact-list li { display: flex; align-items: center; gap: 9px; }
  .contact-list svg { width: 13px; height: 13px; flex: none; fill: var(--teal); }
  .agent-name {
    position: absolute;
    right: 24px; top: 236px;
    font-family: "Cinzel", Georgia, serif;
    font-size: 21px;
    color: var(--white);
    letter-spacing: .5px;
  }
  .agent-title {
    position: absolute;
    right: 22px; top: 342px;
    font-size: 15px;
    color: var(--white);
  }
</style>
</head>
<body>

  <section class="card card-back" aria-label="Business card, back">
    <div class="brand">
      <span class="brand-dot"></span>
      <span class="brand-name">Brockhill<br>Real Estate Services</span>
    </div>
    <p class="offer">Home owners, call today to receive a FREE<br>market analysis for your homes value!</p>
  </section>

  <section class="card card-front" aria-label="Business card, front">
    <svg class="front-bands" viewBox="0 0 660 377" width="660" height="377" aria-hidden="true">
      <defs>
        <linearGradient id="silver" x1="0" y1="0" x2="1" y2="0">
          <stop offset="0" stop-color="var(--silver-1)"/>
          <stop offset=".5" stop-color="var(--silver-2)"/>
          <stop offset="1" stop-color="var(--silver-1)"/>
        </linearGradient>
        <linearGradient id="tealband" x1="0" y1="0" x2="1" y2="1">
          <stop offset="0" stop-color="#1b95a3"/>
          <stop offset="1" stop-color="#0d6e7b"/>
        </linearGradient>
      </defs>
      <path d="M180,318 L200,305 L395,305 L395,312 L205,312 L190,322 Z" fill="url(#silver)"/>
      <path d="M0,377 L0,332 L185,332 L205,318 L395,318 L410,222 L660,222 L660,377 Z" fill="url(#tealband)"/>
      <path d="M0,324 L175,324 L190,314" stroke="url(#silver)" stroke-width="3" fill="none"/>
    </svg>

    <div class="brand">
      <span class="brand-dot"></span>
      <span class="brand-name">Brockhill<br>Real Estate Services</span>
    </div>

    <div class="portrait" role="img" aria-label="Portrait photo of Lorna Vettridge"></div>

    <ul class="contact-list">
      <li>
        <svg viewBox="0 0 24 24"><path d="M6.6 10.8a15.1 15.1 0 0 0 6.6 6.6l2.2-2.2a1 1 0 0 1 1-.25 11.4 11.4 0 0 0 3.6.57 1 1 0 0 1 1 1V20a1 1 0 0 1-1 1A17 17 0 0 1 3 4a1 1 0 0 1 1-1h3.5a1 1 0 0 1 1 1c0 1.25.2 2.45.57 3.57a1 1 0 0 1-.25 1z"/></svg>
        <span>555.218.7094</span>
      </li>
      <li>
        <svg viewBox="0 0 24 24"><path d="M2 5h20v14H2z M2 5l10 8 10-8" /></svg>
        <span>lorna@brockhillhomes.example</span>
      </li>
      <li>
        <svg viewBox="0 0 24 24"><circle cx="12" cy="12" r="10"/></svg>
        <span>www.brockhillhomes.example</span>
      </li>
    </ul>

    <h1 class="agent-name">Lorna Vettridge</h1>
    <p class="agent-title">Owner &amp; Qualifying Broker, Brockhill Real Estate Services</p>
  </section>

</body>
</html>
```